Bref créative
vostelmira #20
Real Estate Investors
Professional
Dale Quistorff
President
8316 Willowmere Rd, Ste. 217 (#492)
Corvell, TX 76218
dquistorff@mailvessa.com
Please make 100 cards in the name of Dale Quistorff and the other 100 cards in the name of: Colette Quistorff, Title: Program Director, Address: Same, Phone: Same, Cell: 214 637-2940, E-mail: colette.quistorff@mailvessa.com.
Keep in mind we will request an update on this card in a later date with the following: Website Address, Fax #, and Toll Free #.

```html
<!DOCTYPE html>
<html lang="en">
<head>
<meta charset="utf-8">
<title>Tolvanex Business Cards</title>
<link href="https://fonts.googleapis.com/css2?family=Cinzel:wght@400;600&family=Libre+Baskerville&display=swap" rel="stylesheet">
<style>
  :root{
    --bg:#3b3b3d;
    --card-dark:#1c1c1e;
    --card-mid:#2a2a2c;
    --red:#d8262e;
    --silver:#c9c9cc;
    --silver-dark:#8c8c90;
    --text-light:#d6d6d8;
    --text-ink:#1e1e20;
  }
  *{margin:0;padding:0;box-sizing:border-box}
  html,body{width:1200px;height:874px;overflow:hidden;background:var(--bg)}
  .stage{position:relative;width:1200px;height:874px;display:flex;align-items:center;justify-content:center;gap:60px}
  .card{position:relative;width:520px;height:300px;border-radius:18px;overflow:hidden;
    background:linear-gradient(135deg,var(--card-mid) 0%,var(--card-dark) 55%,var(--card-mid) 100%);
    box-shadow:0 14px 30px rgba(0,0,0,.45)}
  .brand-name{font-family:'Cinzel',serif;font-weight:600;letter-spacing:2px;line-height:1}
  .tagline{font-family:'Cinzel',serif;font-weight:400;letter-spacing:3.5px;font-size:9px;color:var(--text-light)}

  /* front */
  .front .brand{position:absolute;left:190px;top:112px;display:flex;flex-direction:column;gap:6px}
  .front .brand-name{font-size:46px;color:var(--silver)}
  .front .stripes{position:absolute;left:0;bottom:22px}

  /* back */
  .back .brand{position:absolute;left:34px;top:92px;display:flex;flex-direction:column;gap:6px}
  .back .brand-name{font-size:44px;color:var(--red)}
  .person{position:absolute;right:40px;top:52px;text-align:right;font-family:'Libre Baskerville',serif}
  .person-name{color:var(--red);font-size:17px}
  .person-title{color:var(--text-light);font-size:11px;margin-top:5px}
  .address{position:absolute;left:34px;top:196px;font-family:'Libre Baskerville',serif;font-size:10.5px;color:var(--text-light)}
  .contact-band{position:absolute;left:0;right:0;bottom:0;height:56px;
    background:linear-gradient(180deg,#e4e4e6 0%,var(--silver) 50%,var(--silver-dark) 100%);
    display:flex;align-items:center;justify-content:space-between;padding:0 40px 0 34px;
    font-family:'Libre Baskerville',serif;font-size:12px;color:var(--text-ink)}
  .contact-item{display:flex;align-items:center;gap:7px}
  .back .stripes{position:absolute;right:0;bottom:56px}
</style>
</head>
<body>
<main class="stage">
  <section class="card front" aria-label="Card front">
    <div class="brand">
      <span class="brand-name">TOLVANEX</span>
      <span class="tagline">REAL ESTATE INVESTORS</span>
    </div>
    <svg class="stripes" width="210" height="60" viewBox="0 0 210 60" aria-hidden="true">
      <polygon points="0,8 150,8 140,22 0,22" fill="var(--red)"/>
      <polygon points="0,28 190,28 180,44 0,44" fill="var(--silver)"/>
      <polygon points="0,48 120,48 114,56 0,56" fill="var(--red)"/>
    </svg>
  </section>

  <section class="card back" aria-label="Card back">
    <div class="person">
      <div class="person-name">Dale Quistorff</div>
      <div class="person-title">President</div>
    </div>
    <div class="brand">
      <span class="brand-name">TOLVANEX</span>
      <span class="tagline">REAL ESTATE INVESTORS</span>
    </div>
    <p class="address">8316 Willowmere Rd, Ste. 217 (#492) Corvell, TX 76218</p>
    <svg class="stripes" width="110" height="30" viewBox="0 0 110 30" aria-hidden="true">
      <polygon points="40,6 110,6 110,16 32,16" fill="var(--red)"/>
      <polygon points="20,20 110,20 110,30 12,30" fill="var(--silver)"/>
    </svg>
    <div class="contact-band">
      <span class="contact-item">
        <svg width="14" height="14" viewBox="0 0 24 24" aria-hidden="true"><path d="M6.6 10.8a15 15 0 0 0 6.6 6.6l2.2-2.2a1 1 0 0 1 1-.25 11.4 11.4 0 0 0 3.6.57 1 1 0 0 1 1 1V20a1 1 0 0 1-1 1A17 17 0 0 1 3 4a1 1 0 0 1 1-1h3.5a1 1 0 0 1 1 1c0 1.25.2 2.45.57 3.6a1 1 0 0 1-.25 1z" fill="var(--text-ink)"/></svg>
        214-482-7716
      </span>
      <span class="contact-item">
        <svg width="15" height="12" viewBox="0 0 24 18" aria-hidden="true"><rect x="1" y="1" width="22" height="16" rx="2" fill="none" stroke="var(--text-ink)" stroke-width="2"/><path d="M1 2l11 8 11-8" fill="none" stroke="var(--text-ink)" stroke-width="2"/></svg>
        dquistorff@mailvessa.com
      </span>
    </div>
  </section>
</main>
</body>
</html>
```